Dorrish Electric Ltd

Looking for a single page website and Facebook page design. I am an electrical contractor based on Vancouver Island. I do service, custom homes, residential and commercial installations. My company just started out, so I don't have any pictures of installs yet. I have 25 years experience. I would like the colors to be my logo colors black and I have a black Corvan Ridgeback that will be my vehicle which I will have a wrap for.
Updates

I just posted the contest today, not sure why the deadline is the same day.

Went on vacation/holiday

Industry/Entity Type

Electrician

Requirements
Must have
• Services provided, About me section, quote section,
Nice to have
• I am not quite sure yet, I need to see some designs first .

```html
<!DOCTYPE html>
<html lang="en">
<head>
<meta charset="utf-8">
<title>Dorrish Electric Ltd</title>
<link href="https://fonts.googleapis.com/css2?family=Montserrat:wght@400;500;600;700;800&family=Roboto:wght@400;500;700&display=swap" rel="stylesheet">
<style>
:root{
  --gold:#f2b418;
  --gold-deep:#d99a0b;
  --black:#070707;
  --ink:#111111;
  --panel:#1c1c1c;
  --card:#222222;
  --white:#ffffff;
  --muted:#cfcfcf;
  --grey:#8a8a8a;
}
*{margin:0;padding:0;box-sizing:border-box}
html,body{width:1200px;height:5305px;overflow:hidden;background:var(--black)}
body{font-family:'Roboto',sans-serif;color:var(--white);position:relative}
.abs{position:absolute}
h1,h2,h3,h4{font-family:'Montserrat',sans-serif}
.gold{color:var(--gold)}

/* header */
.topbar{position:absolute;left:0;top:0;width:1200px;height:90px;background:var(--black)}
.brand{position:absolute;left:130px;top:6px;width:130px;text-align:center}
.brand-dot{width:56px;height:56px;border-radius:50%;border:3px solid var(--gold);margin:0 auto 4px}
.brand-name{font-family:'Montserrat',sans-serif;font-weight:700;font-size:10.5px;letter-spacing:.3px;color:var(--white)}
.contact-chip{position:absolute;top:22px;display:flex;align-items:center;gap:14px}
.contact-chip .ic{width:46px;height:46px;border-radius:50%;border:2px solid var(--white);display:flex;align-items:center;justify-content:center}
.contact-chip small{display:block;font-size:10px;color:var(--gold);font-weight:700;letter-spacing:.5px}
.contact-chip span{font-size:17px}
.mainnav{position:absolute;left:0;top:90px;width:1200px;height:58px;background:var(--gold)}
.mainnav a{position:absolute;top:0;height:58px;line-height:58px;font-family:'Montserrat',sans-serif;font-weight:700;font-size:11.5px;color:var(--white);text-decoration:none;transform:translateX(-50%)}
.mainnav a.active{background:var(--gold-deep);padding:0 26px}

/* hero */
.hero{position:absolute;left:0;top:148px;width:1200px;height:600px;background:linear-gradient(120deg,#3a3530 0%,#6b6862 35%,#8b8a86 55%,#4b4a47 80%,#2b2825 100%)}
.hero-shade{position:absolute;inset:0;background:rgba(0,0,0,.35)}
.hero-text{position:absolute;left:0;width:1200px;text-align:center}
.hero .kicker{top:172px;font-family:'Montserrat',sans-serif;font-weight:700;font-size:20px}
.hero h1{top:198px;font-size:78px;font-weight:800;letter-spacing:1px}
.hero h1 .thin{font-weight:700}
.hero p{top:290px;left:170px;width:860px;font-size:13.5px;line-height:28px}
.btn{position:absolute;height:46px;border-radius:23px;background:var(--gold);display:flex;align-items:center;font-family:'Montserrat',sans-serif;font-weight:700;font-size:15px;color:var(--white);padding:0 30px 0 6px;gap:16px}
.btn .bdot{width:36px;height:36px;border-radius:50%;border:2px solid var(--white)}
.dots{position:absolute;top:566px;left:0;width:1200px;display:flex;justify-content:center;gap:6px}
.dots i{width:11px;height:11px;border-radius:50%;background:var(--white)}
.dots i.off{background:transparent;border:2px solid var(--white)}

/* section titles */
.sec-title{position:absolute;left:0;width:1200px;text-align:center;font-size:36px;font-weight:700}
.sec-title::after{content:"";display:block;width:54px;height:4px;background:var(--gold);margin:10px auto 0}

/* services */
.services{position:absolute;left:0;top:748px;width:1200px;height:628px;background:var(--black)}
.svc{position:absolute;top:190px;width:300px;text-align:center;transform:translateX(-50%)}
.svc svg{display:block;margin:0 auto}
.svc h3{font-size:20px;font-weight:600;margin-top:18px;letter-spacing:.5px}
.svc p{font-size:14px;line-height:33px;margin-top:6px}
.svc .more{font-size:12px;font-weight:500;color:var(--grey);margin-top:4px;letter-spacing:.5px}
.svc.on h3{color:var(--gold)}
.svc.on .more{color:var(--white);text-decoration:underline;text-decoration-color:var(--gold);text-underline-offset:4px}

/* about */
.about{position:absolute;left:0;top:1376px;width:1200px;height:447px;background:var(--panel);overflow:hidden}
.about p{position:absolute;left:42px;top:40px;width:385px;font-size:12.8px;line-height:28px}
.about-side{position:absolute;right:0;top:0;width:260px;height:447px;background:var(--gold)}
.about-side .vert{position:absolute;left:110px;top:64px;writing-mode:vertical-rl;font-family:'Montserrat',sans-serif;font-weight:700;font-size:31px;color:var(--white);letter-spacing:1px}
.about-mark{position:absolute;left:440px;top:-2px;width:560px;height:450px}

/* why */
.why{position:absolute;left:0;top:1823px;width:1200px;height:855px;background:var(--black);overflow:hidden}
.why-item{position:absolute;width:300px}
.why-item h4{font-size:15px;font-weight:600;color:var(--gold);letter-spacing:.3px}
.why-item p{font-size:11px;line-height:23px;margin-top:6px}
.why-item.r{text-align:right}
.why-ic{position:absolute;width:86px;height:86px;border-radius:50%;border:2px solid var(--white);display:flex;align-items:center;justify-content:center;transform:translate(-50%,-50%);background:var(--black)}
.why-ic.fill{background:var(--gold);border-color:var(--gold);width:90px;height:90px}

/* team */
.team{position:absolute;left:0;top:2678px;width:1200px;height:649px;background:linear-gradient(180deg,#1a1a1a,#101010)}
.member{position:absolute;top:200px;width:226px;height:358px;transform:translateX(-50%);text-align:center;background:#141414}
.member.on{border:2px solid var(--gold);top:196px}
.member .ph{width:204px;height:204px;border-radius:50%;margin:10px auto 0;border:4px solid #e6e6e6}
.member h4{font-size:16px;font-weight:700;margin-top:18px;letter-spacing:.5px}
.member p{font-size:12.5px;line-height:28px;margin-top:4px;padding:0 10px}

/* testimonials */
.testi{position:absolute;left:0;top:3327px;width:1200px;height:649px;background:var(--black)}
.tcard{position:absolute;top:196px;width:437px;height:251px;background:var(--card)}
.tcard .av{position:absolute;left:22px;top:28px;width:96px;height:96px;border-radius:50%;border:3px solid #e6e6e6}
.tcard h4{position:absolute;left:138px;top:32px;font-size:17px;font-weight:600;color:var(--gold)}
.tcard .sub{position:absolute;left:138px;top:58px;font-size:13.5px;display:flex;gap:14px;align-items:center}
.tcard .stars{color:var(--gold);font-size:13px;letter-spacing:1px}
.tcard .q{position:absolute;left:28px;top:132px;font-family:Georgia,serif;font-size:120px;line-height:1;color:#5a5a5a}
.tcard p{position:absolute;left:138px;top:86px;width:280px;font-size:11.5px;line-height:28px;text-align:justify}
.tcard .corner{position:absolute;right:0;bottom:0;width:20px;height:20px;background:var(--gold-deep)}

/* member cta */
.cta{position:absolute;left:0;top:3976px;width:1200px;height:556px;background:var(--panel)}
.cta h2{position:absolute;left:130px;font-size:37px}
.cta .l1{top:80px;font-weight:400}
.cta .l2{top:128px;font-weight:700;color:var(--gold)}
.cta p{position:absolute;left:130px;top:200px;width:500px;font-size:14px;line-height:28px}
.cta-photo{position:absolute;left:640px;top:-52px;width:432px;height:608px;border-radius:216px 216px 0 0;background:linear-gradient(180deg,#5d4b3a 0%,#2b3242 60%,#1d2230 100%)}
.cta-ring{position:absolute;left:660px;top:90px;width:440px;height:440px;border-radius:50%;border:6px solid var(--white);border-right-color:transparent;border-bottom-color:transparent}

/* contact */
.contact{position:absolute;left:132px;top:4402px;width:935px;height:511px;background:var(--gold);overflow:hidden}
.contact h2{position:absolute;left:0;width:935px;text-align:center;font-size:34px}
.contact .c1{top:50px;font-weight:400}
.contact .c2{top:96px;font-weight:700}
.field{position:absolute;background:#fcf3d6;font-size:12px;color:#7a6a44;padding:20px 0 0 22px}
.skyline{position:absolute;left:0;bottom:0;width:935px;height:170px;background:linear-gradient(180deg,rgba(242,180,24,0) 0%,rgba(60,45,10,.35) 55%,rgba(30,22,5,.75) 100%)}
.btn.dark{background:var(--gold);border:2px solid var(--white)}

/* footer */
.footer{position:absolute;left:0;top:4913px;width:1200px;height:392px;background:var(--black)}
.fcol{position:absolute;top:82px}
.fcol h4{font-size:16px;font-weight:700;letter-spacing:.5px;margin-bottom:14px}
.fcol li{list-style:none;font-size:12px;line-height:28px;display:flex;gap:10px;align-items:flex-start}
.fcol li b{color:var(--white);font-weight:700;font-size:11px}
.fbrand{position:absolute;left:852px;top:78px;width:200px;text-align:center}
.fbrand .brand-dot{width:80px;height:80px}
.fbrand .nm{font-family:'Montserrat',sans-serif;font-weight:600;font-size:13px;margin-top:6px}
.fbrand small{display:block;font-size:12px;color:var(--gold);font-weight:700;margin-top:20px}
.fbrand span{display:block;font-size:12px;font-weight:700;margin-top:4px}
.frule{position:absolute;left:148px;top:270px;width:918px;height:1px;background:#666}
.copy{position:absolute;left:0;top:290px;width:1200px;text-align:center;font-size:12px}
.socials{position:absolute;left:0;top:322px;width:1200px;display:flex;justify-content:center;gap:10px}
.socials i{width:30px;height:30px;border-radius:50%;border:2px solid var(--gold)}
</style>
</head>
<body>

<header class="topbar">
  <div class="brand">
    <div class="brand-dot"></div>
    <div class="brand-name">DORRISH ELECTRIC Ltd</div>
  </div>
  <div class="contact-chip" style="left:500px">
    <div class="ic"><svg width="22" height="22" viewBox="0 0 24 24" fill="none" stroke="#fff" stroke-width="1.8"><path d="M5 3h4l2 5-3 2a12 12 0 0 0 6 6l2-3 5 2v4a2 2 0 0 1-2 2A18 18 0 0 1 3 5a2 2 0 0 1 2-2z"/></svg></div>
    <div><small>CALL NOW :</small><span>+1 (250) 555 0142</span></div>
  </div>
  <div class="contact-chip" style="left:745px">
    <div class="ic"><svg width="22" height="22" viewBox="0 0 24 24" fill="none" stroke="#fff" stroke-width="1.8"><rect x="3" y="5" width="18" height="14" rx="2"/><path d="M3 7l9 6 9-6"/></svg></div>
    <div><small>EMAIL :</small><span>info@dorrishelectric.com</span></div>
  </div>
</header>

<nav class="mainnav">
  <a class="active" style="left:220px">HOME</a>
  <a style="left:317px">ABOUT US</a>
  <a style="left:439px">OUR SERVICES</a>
  <a style="left:581px">WHY CHOOSE US</a>
  <a style="left:725px">TESTIMONIALS</a>
  <a style="left:845px">GALLERY</a>
  <a style="left:958px">CONTACT US</a>
</nav>

<section class="hero" role="img" aria-label="Electrician's hands working on wiring in an electrical panel">
  <div class="hero-shade"></div>
  <div class="hero-text kicker">WELCOME TO</div>
  <h1 class="hero-text">DORRISH <span class="gold">ELECTRIC</span> <span class="thin">Ltd</span></h1>
  <p class="hero-text">Lorem ipsum dolor sit amet, consectetur adipiscing elit, sed do eiusmod tempor incididunt ut labore et dolore magna aliqua. Quis ipsum suspendisse ultrices gravida. Risus commodo viverra maecenas accumsan lacus vel facilisis.</p>
  <div class="btn" style="left:502px;top:374px"><span class="bdot"></span>GET STARTED</div>
  <div class="dots"><i></i><i></i><i class="off"></i><i></i><i></i></div>
</section>

<section class="services">
  <h2 class="sec-title" style="top:88px">OUR <span class="gold">SERVICES</span></h2>

  <div class="svc" style="left:294px">
    <svg width="160" height="160" viewBox="0 0 160 160" fill="none">
      <circle cx="80" cy="80" r="72" stroke="#fff" stroke-width="4"/>
      <path d="M80 8a72 72 0 0 1 62 108" stroke="#f2b418" stroke-width="8"/>
      <rect x="50" y="52" width="60" height="56" stroke="#f2b418" stroke-width="3"/>
      <path d="M58 98l40-36M90 60l10 10" stroke="#fff" stroke-width="3"/>
    </svg>
    <h3>CUSTOM HOMES</h3>
    <p>Lorem ipsum dolor sit amet, con-<br>sectetur adipiscing elit, sed do eius-<br>mod tempor incididunt ut.</p>
    <div class="more">LEARN MORE</div>
  </div>

  <div class="svc on" style="left:601px">
    <svg width="160" height="160" viewBox="0 0 160 160" fill="none">
      <circle cx="80" cy="80" r="72" stroke="#fff" stroke-width="4"/>
      <path d="M80 8a72 72 0 0 1 62 108" stroke="#f2b418" stroke-width="8"/>
      <path d="M46 78l34-28 34 28" stroke="#fff" stroke-width="3"/>
      <rect x="54" y="76" width="52" height="34" stroke="#f2b418" stroke-width="3"/>
      <rect x="72" y="90" width="16" height="20" stroke="#fff" stroke-width="3"/>
    </svg>
    <h3>RESIDENTIAL</h3>
    <p>Lorem ipsum dolor sit amet, con-<br>sectetur adipiscing elit, sed do eius-<br>mod tempor incididunt ut.</p>
    <div class="more">LEARN MORE</div>
  </div>

  <div class="svc" style="left:908px">
    <svg width="160" height="160" viewBox="0 0 160 160" fill="none">
      <circle cx="80" cy="80" r="72" stroke="#fff" stroke-width="4"/>
      <path d="M80 8a72 72 0 0 1 62 108" stroke="#f2b418" stroke-width="8"/>
      <rect x="58" y="54" width="28" height="56" stroke="#fff" stroke-width="3"/>
      <rect x="86" y="70" width="18" height="40" stroke="#f2b418" stroke-width="3"/>
      <path d="M64 64h16M64 76h16M64 88h16" stroke="#f2b418" stroke-width="3"/>
    </svg>
    <h3>COMMERCIAL</h3>
    <p>Lorem ipsum dolor sit amet, con-<br>sectetur adipiscing elit, sed do eius-<br>mod tempor incididunt ut.</p>
    <div class="more">LEARN MORE</div>
  </div>
</section>

<section class="about">
  <p>Lorem ipsum dolor sit amet, consectetur adipiscing elit, sed do eiusmod tempor incididunt ut labore et dolore magna aliqua. Quis ipsum suspendisse ultrices gravida. Risus commodo viverra maecenas accumsan lacus vel facilisis. Lorem ipsum dolor sit amet, consectetur adipiscing elit, sed do eiusmod tempor incididunt ut labore et dolore magna aliqua. Ut enim ad minim veniam, quis nostrud exercitation ullamco laboris nisi ut aliquip ex ea commodo consequat. Duis aute irure dolor in reprehenderit in voluptate velit esse cillum dolore eu fugiat nulla pariatur. Excepteur sint occaecat cupidatat non proident.</p>
  <div class="btn" style="left:42px;top:348px"><span class="bdot"></span>LEARN MORE</div>
  <div class="about-side"><div class="vert">ABOUT DORRISH</div></div>
  <svg class="about-mark" viewBox="0 0 560 450" fill="none">
    <path d="M300 -10 A300 300 0 0 1 560 230 L560 450 L380 450 A240 240 0 0 0 300 -10z" fill="#f2b418"/>
    <circle cx="270" cy="225" r="222" fill="#0d0d0d" stroke="#e8e8e8" stroke-width="6"/>
    <text x="270" y="234" text-anchor="middle" font-family="Montserrat, sans-serif" font-weight="700" font-size="28" fill="#ffffff">DORRISH ELECTRIC Ltd</text>
  </svg>
</section>

<section class="why">
  <h2 class="sec-title" style="top:120px">WHY <span class="gold">CHOOSE US</span></h2>
  <svg class="abs" style="left:0;top:0" width="1200" height="855" viewBox="0 0 1200 855" fill="none">
    <path d="M150 855 A445 445 0 1 1 1036 855" stroke="#f2b418" stroke-width="4"/>
    <path d="M140 855 A455 455 0 0 1 170 640" stroke="#f2b418" stroke-width="2"/>
    <path d="M1046 855 A455 455 0 0 0 1016 640" stroke="#f2b418" stroke-width="2"/>
    <path d="M240 495 H950 M240 643 H950" stroke="#6a6a6a" stroke-width="1.5" stroke-dasharray="3 4"/>
    <circle cx="593" cy="573" r="108" fill="#0d0d0d" stroke="#fff" stroke-width="5"/>
    <path d="M593 465 A108 108 0 0 1 593 681" stroke="#f2b418" stroke-width="9"/>
    <text x="593" y="580" text-anchor="middle" font-family="Montserrat, sans-serif" font-weight="700" font-size="16" fill="#ffffff">DORRISH ELECTRIC Ltd</text>
  </svg>

  <div class="why-ic fill" style="left:255px;top:402px"><svg width="40" height="40" viewBox="0 0 24 24" fill="none" stroke="#fff" stroke-width="1.6"><circle cx="12" cy="8" r="4"/><path d="M4 21a8 8 0 0 1 16 0"/></svg></div>
  <div class="why-item" style="left:321px;top:362px"><h4>LICENSED EXPERTS</h4><p>Sed ut perspiciatis unde omnis iste<br>natus error sit voluptatem accusantium</p></div>

  <div class="why-item r" style="left:553px;top:360px"><h4>24/7 SERVICE AVAILABLE</h4><p>Sed ut perspiciatis unde omnis iste<br>natus error sit voluptatem accusantium</p></div>
  <div class="why-ic" style="left:917px;top:402px"><svg width="36" height="36" viewBox="0 0 24 24" fill="none" stroke="#fff" stroke-width="1.6"><path d="M5 3h4l2 5-3 2a12 12 0 0 0 6 6l2-3 5 2v4a2 2 0 0 1-2 2A18 18 0 0 1 3 5a2 2 0 0 1 2-2z"/></svg></div>

  <div class="why-ic" style="left:175px;top:567px"><svg width="36" height="36" viewBox="0 0 24 24" fill="none" stroke="#fff" stroke-width="1.6"><circle cx="12" cy="10" r="7"/><path d="M9 10l2 2 4-4M8 16l-2 6 6-3 6 3-2-6"/></svg></div>
  <div class="why-item" style="left:245px;top:527px"><h4>LABOUR GUARANTEED</h4><p>Sed ut perspiciatis unde omnis iste<br>natus error sit voluptatem accusantium</p></div>

  <div class="why-item r" style="left:633px;top:527px"><h4>SPECIAL OFFERS</h4><p>Sed ut perspiciatis unde omnis iste<br>natus error sit voluptatem accusantium</p></div>
  <div class="why-ic" style="left:1003px;top:567px"><svg width="36" height="36" viewBox="0 0 24 24" fill="none" stroke="#fff" stroke-width="1.6"><path d="M3 12l9-9h8v8l-9 9z"/><circle cx="16" cy="8" r="1.5"/></svg></div>

  <div class="why-ic" style="left:165px;top:735px"><svg width="36" height="36" viewBox="0 0 24 24" fill="none" stroke="#fff" stroke-width="1.6"><rect x="4" y="3" width="16" height="18" rx="2"/><path d="M8 8h8M8 12h8M8 16h5"/></svg></div>
  <div class="why-item" style="left:235px;top:694px"><h4>FIXED FEE PRICING</h4><p>Sed ut perspiciatis unde omnis iste<br>natus error sit voluptatem accusantium</p></div>

  <div class="why-item r" style="left:646px;top:707px"><h4>100% SATISFATO GUARANTEED</h4><p>Sed ut perspiciatis unde omnis iste<br>natus error sit voluptatem accusantium</p></div>
  <div class="why-ic" style="left:1013px;top:735px"><svg width="36" height="36" viewBox="0 0 24 24" fill="none" stroke="#fff" stroke-width="1.6"><circle cx="12" cy="9" r="6"/><path d="M8 14l-2 8 6-3 6 3-2-8"/></svg></div>
</section>

<section class="team">
  <h2 class="sec-title" style="top:96px">MEET <span class="gold">OUR TEAM</span></h2>
  <div class="member" style="left:243px"><div class="ph" role="img" aria-label="Portrait of electrician holding tools" style="background:linear-gradient(160deg,#c8c2b8,#6d5a3f)"></div><h4>JOHN SMITH</h4><p>Lorem ipsum dolor sit amet, con-sectetur adipiscing elit, sed do eiusmod tempo.</p></div>
  <div class="member on" style="left:480px"><div class="ph" role="img" aria-label="Portrait of electrician in red hard hat with clipboard" style="background:linear-gradient(160deg,#a9a9a9,#3a3d44)"></div><h4>JOHN SMITH</h4><p>Lorem ipsum dolor sit amet, con-sectetur adipiscing elit, sed do eiusmod tempo.</p></div>
  <div class="member" style="left:719px"><div class="ph" role="img" aria-label="Portrait of electrician in yellow hard hat" style="background:linear-gradient(160deg,#e8e6e0,#8f8a7e)"></div><h4>JOHN SMITH</h4><p>Lorem ipsum dolor sit amet, con-sectetur adipiscing elit, sed do eiusmod tempo.</p></div>
  <div class="member" style="left:958px"><div class="ph" role="img" aria-label="Portrait of electrician in blue hard hat at a panel" style="background:linear-gradient(160deg,#9fb2c8,#2f4561)"></div><h4>JOHN SMITH</h4><p>Lorem ipsum dolor sit amet, con-sectetur adipiscing elit, sed do eiusmod tempo.</p></div>
</section>

<section class="testi">
  <h2 class="sec-title" style="top:98px">OUR <span class="gold">CLIENT TESTIMONIALS</span></h2>
  <div class="tcard" style="left:144px">
    <div class="av" role="img" aria-label="Client portrait" style="background:linear-gradient(160deg,#d7c7b0,#6b5a44)"></div>
    <h4>John Deo</h4>
    <div class="sub">Lorem ipsum set <span class="stars">★★★★★</span></div>
    <div class="q">“</div>
    <p>Nemo enim ipsam voluptatem quia voluptas sit aspernatur aut odit aut fugit, sed quia consequuntur magni dolores eos qui ratione voluptatem sequi nesciunt aut fugit, sed quia consequuntur magni.</p>
    <div class="corner"></div>
  </div>
  <div class="tcard" style="left:620px">
    <div class="av" role="img" aria-label="Client portrait" style="background:linear-gradient(160deg,#b8c2cc,#3f4a55)"></div>
    <h4>John Deo</h4>
    <div class="sub">Lorem ipsum set <span class="stars">★★★★★</span></div>
    <div class="q">“</div>
    <p>Nemo enim ipsam voluptatem quia voluptas sit aspernatur aut odit aut fugit, sed quia consequuntur magni dolores eos qui ratione voluptatem sequi nesciunt aut fugit, sed quia consequuntur magni.</p>
    <div class="corner"></div>
  </div>
  <div class="btn" style="left:502px;top:512px;padding-right:52px;gap:30px"><span class="bdot"></span>VIEW ALL</div>
</section>

<section class="cta">
  <div class="cta-photo" role="img" aria-label="Smiling electrician in hard hat with coiled cable, arms crossed"></div>
  <div class="cta-ring"></div>
  <h2 class="l1">BECOME A DORRISH</h2>
  <h2 class="l2">PLUS MEMBER TODAY</h2>
  <p>Lorem ipsum dolor sit amet, consectetur adipiscing elit, sed do eiusmod tempor incididunt ut labore et dolore magna aliqua. Quis ipsum suspendisse ultrices gravida. Risus commodo viverra maecenas accumsan lacus vel facilisis.</p>
  <div class="btn" style="left:130px;top:328px"><span class="bdot"></span>+1 250 555 0142</div>
</section>

<section class="contact">
  <div class="skyline" role="img" aria-label="City skyline silhouette"></div>
  <h2 class="c1">CONTACT US</h2>
  <h2 class="c2">CONTACT DORRISH ELECTRICAL TODAY</h2>
  <div class="field" style="left:64px;top:161px;width:397px;height:52px">First name</div>
  <div class="field" style="left:476px;top:161px;width:397px;height:52px">Last Name</div>
  <div class="field" style="left:64px;top:229px;width:397px;height:50px">Phone Numbers</div>
  <div class="field" style="left:476px;top:229px;width:397px;height:50px">Email address</div>
  <div class="field" style="left:64px;top:299px;width:809px;height:95px">Message</div>
  <div class="btn dark" style="left:362px;top:414px;padding-right:32px"><span class="bdot"></span>SUBMIT NOW</div>
</section>

<footer class="footer">
  <div class="fcol" style="left:148px"><h4>QUICK LINKS</h4><ul>
    <li><b>»</b>Home</li><li><b>»</b>About Us</li><li><b>»</b>Our Services</li><li><b>»</b>Why Choose Us</li><li><b>»</b>Testimonials</li></ul></div>
  <div class="fcol" style="left:381px"><h4>LEGAL</h4><ul>
    <li><b>»</b>Terms of Use</li><li><b>»</b>Privacy Policy</li><li><b>»</b>Gallery</li><li><b>»</b>Contact Us</li></ul></div>
  <div class="fcol" style="left:583px"><h4>CONTACT US</h4><ul>
    <li><svg width="12" height="14" viewBox="0 0 24 28"><path d="M12 0a10 10 0 0 1 10 10c0 8-10 18-10 18S2 18 2 10A10 10 0 0 1 12 0z" fill="#fff"/><circle cx="12" cy="10" r="4" fill="#070707"/></svg><span>123 Lorem ipsum dolor sit amet,<br>consectetur adipiscing eli.</span></li>
    <li style="margin-top:6px"><svg width="13" height="13" viewBox="0 0 24 24"><path d="M5 3h4l2 5-3 2a12 12 0 0 0 6 6l2-3 5 2v4a2 2 0 0 1-2 2A18 18 0 0 1 3 5a2 2 0 0 1 2-2z" fill="#fff"/></svg>+1 250 555 0142</li>
    <li style="margin-top:14px"><svg width="13" height="13" viewBox="0 0 24 24"><rect x="2" y="5" width="20" height="14" fill="#fff"/></svg>info@dorrishelectric.com</li></ul></div>
  <div class="fbrand">
    <div class="brand-dot"></div>
    <div class="nm">DORRISH ELECTRIC Ltd</div>
    <small>Hours:</small>
    <span>Monday - Friday 7:00am - 5:00pm</span>
  </div>
  <div class="frule"></div>
  <div class="copy">© Copyrights 2022 &nbsp;<b>DORRISH <span class="gold">ELECTRIC</span> Ltd</b> &nbsp;| &nbsp; All Rights Reserved</div>
  <div class="socials"><i></i><i></i><i></i><i></i></div>
</footer>

</body>
</html>
```